We need to design a new tradeshow booth for our company. We are Veltrane Engraving Systems and are the Authorized Distributor of laser products for QR Dyne. We are basically the USA branch of their group, representing their products. We stock, sell and distribute laser systems for this company. QRDyne is located in China. We also sell pad printing equipment and supplies, although this business is slowly becoming smaller as we focus more on lasers.

The parameters for the booth are as follows:

1) Our company logo should be on the tradeshow booth, as well as the QR Dyne logo. The QRDyne logo is provided and so will ours.
2) We would like to keep the tradeshow booth clean looking so the message comes across what we do very clear.
3) Pad printing should be emphasized on only one of the stands (attaches as file D), while the other stand (attached as file D) should emphasize laser products.
4) Laser Marking, Welding, Cleaning and Cutting are the four segments in which we operate. These make up the core of what lasers can do in a manufacturing environment. Most companies offer only specialize in one area but we can offer all four with the ability to supply 12 kilowatts of laser power, which is enough to cut through 40 mm of stainless steel.
5) Laser sources are many and operate in different wavelengths. Most companies only offer one source. We use four: Fiber, UV, CO2, and Green.
6) Continuous wave and Pulsed Options with Pico and Femto Lasers Available
7) Process Stationary and Moving Parts - Perfect for marking in packaging operations or on extrusion machinery.
8) Mark Graphics, Words, Bar codes, QR Codes and more. Maybe this gets incorporated next to marking section?
9) We custom build this machinery so we tailor it to the customer’s requirements with robotic integration possible.
10) Lasers Process Circuit Boards - Cut, Mark and Bore Holes that leave products much higher quality than traditional routers.
11) On pad printing graphic (One of the D Stands) - we custom design pad printing machinery 1-5 color with pneumatic and servo controls available. We offer, pads, cliches, rings, ink and other operating supplies. Same day shipping.
12) All designs should be vector files in AI or PDF format - 95 dpi is required.
13) If vector file logos are required we can supply for final booth design. Logos uploaded can be used as temporary logos.
14) www.qrbeamusa-example.com website should be somewhere on the booth - under the QRDyne logo?
15) A QR code pointing to our site (www.veltrane-example.com) should be on the booth, as well.
16) We May select your design but want to incorporate/add/amend/append final design depending on our team’s feedback.
17) Am example of the booth layout is attached but this should not be referenced for inspiration. We do not need our booth to look like this. It is just for general layout guidelines. THE “E” SECTION OF THE BOOTH WILL NOT STICK OUT LIKE THE ONE IN THE PHOTO. It is all one plane against the wall of the booth.

Thank you for taking the time to look at this.

Target Market(s)

Industrial Automation - Medical, Automotive, Packaging, Metal Processing

Industry/Entity Type

Industrial

Colors

Designer to choose colors to be used in the design.

Requirements
Must have
• A clean crisp feel. We are a fan of Plume’s use of simple straightforward marketing showing our product and what it can do.
• We cannot change the QR Dyne logo. This logo must be present on the tradeshow booth
Nice to have
• Please see the above notes in project description.
Should not have
• A dark theme. We like to keep things open and positive, so the tones of the booth should align with that.

```html
<!DOCTYPE html>
<html lang="en">
<head>
<meta charset="utf-8">
<title>Veltrane Engraving Systems – Booth Panel B</title>
<link href="https://fonts.googleapis.com/css2?family=Source+Sans+3:wght@400;600;700&display=swap" rel="stylesheet">
<style>
  :root {
    --page-bg: #ffffff;
    --panel-bg: #f4f4f6;
    --ink-navy: #2a2f45;
    --ink-body: #1c1d22;
    --accent-blue: #7193d2;
    --ring-grey: #d6d7db;
    --band-light: #dcdde1;
    --band-mid: #b9bbc2;
    --band-dark: #2b3148;
    --band-slate: #4a5264;
    --brand-red: #e0262b;
    --caption-grey: #8a8a8a;
  }
  * { margin: 0; padding: 0; box-sizing: border-box; }
  html, body {
    width: 1200px; height: 994px; overflow: hidden;
    background: var(--page-bg);
    font-family: "Source Sans 3", "Myriad Pro", Arial, sans-serif;
  }
  .canvas { position: relative; width: 1200px; height: 994px; }
  .booth-panel {
    position: absolute; left: 86px; top: 85px;
    width: 1029px; height: 822px;
    background: linear-gradient(135deg, #f0f0f2 0%, #f8f8f9 55%, #f1f1f4 100%);
    overflow: hidden;
  }
  .panel-decor { position: absolute; inset: 0; }
  .brand-mark {
    position: absolute; right: 62px; top: 62px;
    display: flex; align-items: center; gap: 10px;
    color: var(--ink-body);
    font-weight: 700; font-size: 25px; line-height: 1.05;
  }
  .brand-mark .dot {
    width: 30px; height: 30px; border-radius: 50%;
    background: var(--accent-blue); flex: none;
  }
  .headline {
    position: absolute; left: 88px; top: 160px;
    color: var(--ink-navy);
    font-weight: 700; font-size: 50px; line-height: 60px;
    letter-spacing: 0.2px;
  }
  .intro {
    position: absolute; left: 88px; top: 290px;
    color: var(--ink-body);
    font-weight: 400; font-size: 37px; line-height: 44px;
  }
  .service {
    position: absolute; top: 424px; width: 200px;
    text-align: center;
  }
  .service svg { display: block; margin: 0 auto; overflow: visible; }
  .service-name {
    margin-top: 8px;
    color: var(--ink-navy);
    font-weight: 600; font-size: 23px;
  }
  .partner-mark {
    position: absolute; right: 48px; bottom: 36px;
    display: flex; align-items: center; gap: 8px;
    color: var(--ink-body);
    font-weight: 700; font-size: 21px; letter-spacing: 1px;
  }
  .partner-mark .dot {
    width: 16px; height: 16px; border-radius: 50%;
    background: var(--brand-red);
  }
  .panel-caption {
    position: absolute; top: 920px; left: 0; width: 1200px;
    text-align: center; color: var(--caption-grey);
    font-size: 22px; font-weight: 400;
  }
</style>
</head>
<body>
<div class="canvas">
  <section class="booth-panel">
    <svg class="panel-decor" width="1029" height="822" viewBox="0 0 1029 822" aria-hidden="true">
      <polygon points="0,0 60,0 290,180 230,180 0,30" fill="#e4e5e8" opacity="0.8"/>
      <polygon points="70,0 140,0 330,150 300,175" fill="#dcdde1" opacity="0.7"/>
      <polygon points="160,0 230,0 310,70 280,80" fill="#e8e8eb" opacity="0.8"/>
      <path d="M0,710 L230,710 Q260,710 285,735 L370,822 L0,822 Z" fill="var(--band-mid)" opacity="0.55"/>
      <path d="M0,710 L230,710 Q260,710 285,735 L370,822 L330,822 L250,742 Q232,726 210,726 L0,726 Z" fill="#e6e7ea"/>
      <polygon points="0,614 226,822 0,822" fill="var(--band-dark)"/>
      <path d="M0,758 L110,758 Q135,758 160,780 L290,822 L0,822 Z" fill="var(--band-slate)" opacity="0.85"/>
      <polygon points="0,614 226,822 150,822 0,690" fill="#363d52" opacity="0.6"/>
      <polygon points="740,680 790,680 950,822 890,822" fill="#dfe0e3" opacity="0.8"/>
      <polygon points="810,680 860,680 1020,822 960,822" fill="#e6e7ea" opacity="0.8"/>
      <rect x="860" y="762" width="169" height="60" fill="var(--band-mid)" opacity="0.7"/>
    </svg>

    <div class="brand-mark"><span class="dot"></span><span>Veltrane<br>Engraving Systems</span></div>

    <h1 class="headline">LEADING MANUFACTURER OF<br>INDUSTRIAL LASER EQUIPMENT</h1>
    <p class="intro">We offer the finest laser marking, welding<br>and cutting machinery in the marketplace</p>

    <div class="service" style="left:70px">
      <svg width="200" height="200" viewBox="0 0 200 200">
        <circle cx="100" cy="100" r="94" fill="none" stroke="var(--ring-grey)" stroke-width="1.5"/>
        <circle cx="100" cy="100" r="82" fill="#e9eaec" role="img" aria-label="Photo of a laser marking workstation"/>
        <path d="M160.4,28 A94,94 0 1 1 23,153.9" fill="none" stroke="var(--accent-blue)" stroke-width="6" stroke-linecap="round"/>
      </svg>
      <div class="service-name">Laser Marking</div>
    </div>
    <div class="service" style="left:300px">
      <svg width="200" height="200" viewBox="0 0 200 200">
        <circle cx="100" cy="100" r="94" fill="none" stroke="var(--ring-grey)" stroke-width="1.5"/>
        <circle cx="100" cy="100" r="82" fill="#e9eaec" role="img" aria-label="Photo of a laser welding workstation"/>
        <path d="M160.4,28 A94,94 0 1 1 23,153.9" fill="none" stroke="var(--accent-blue)" stroke-width="6" stroke-linecap="round"/>
      </svg>
      <div class="service-name">Laser Welding</div>
    </div>
    <div class="service" style="left:529px">
      <svg width="200" height="200" viewBox="0 0 200 200">
        <circle cx="100" cy="100" r="94" fill="none" stroke="var(--ring-grey)" stroke-width="1.5"/>
        <circle cx="100" cy="100" r="82" fill="#e9eaec" role="img" aria-label="Photo of an enclosed laser cutting machine"/>
        <path d="M160.4,28 A94,94 0 1 1 23,153.9" fill="none" stroke="var(--accent-blue)" stroke-width="6" stroke-linecap="round"/>
      </svg>
      <div class="service-name">Laser Cutting</div>
    </div>
    <div class="service" style="left:759px">
      <svg width="200" height="200" viewBox="0 0 200 200">
        <circle cx="100" cy="100" r="94" fill="none" stroke="var(--ring-grey)" stroke-width="1.5"/>
        <circle cx="100" cy="100" r="82" fill="#e9eaec" role="img" aria-label="Photo of a laser cleaning machine"/>
        <path d="M160.4,28 A94,94 0 1 1 23,153.9" fill="none" stroke="var(--accent-blue)" stroke-width="6" stroke-linecap="round"/>
      </svg>
      <div class="service-name">Laser Cleaning</div>
    </div>

    <div class="partner-mark"><span class="dot"></span><span>QRDYNE</span></div>
  </section>
  <div class="panel-caption">Panel B</div>
</div>
</body>
</html>
```